Stationary and business cards for TerraQuestia-an Education, Enrichment, and Conservation Ctr
TerraQuestia (top line) Education, Enrichment, Conservation
Stationary and business cards for TerraQuestia-an Education, Enrichment, and Conservation Ctr - Animals
Creative Brief
Bright & Fun-filled
Tova Ruth Kellerby-Doane
Executive Director
483 Brindwick Rd. suite 300 Ostervale, MD 20947
tovark@mailcove.example
www.TerraQuestia.example
I would like it to have foliage or vines coming out of the sides like rainforest...maybe a red eye tree frog somewhere and a morpho butterfly... Want it to be simple but classy....and want to be able to have the names and contact info to be interchangeable for all my employees. For the stationary I want the logo somewhere as well. Thank you!
The logo
tovark tovark
I like the leaf addition, but instead of putting it in the back...can you replace the lines in the front of the business card and putting the leaf outlines? That goes better with our theme than "professional" looking lines etc.... thanks!
I can't find how to attach the logo?
quintonhalvard7314065 quintonhalvard7314065
i need the logo logo are not attach in Brief
you can go to our website to get an idea of who we are www.TerraQuestia.example and see our logo.

```html
<!DOCTYPE html>
<html lang="en">
<head>
<meta charset="utf-8">
<title>TerraQuestia Business Cards</title>
<link href="https://fonts.googleapis.com/css2?family=Open+Sans:wght@400;600;700&display=swap" rel="stylesheet">
<style>
  :root {
    --backdrop: #2a2a2a;
    --card: #ffffff;
    --ink: #222222;
    --ink-soft: #444444;
    --leaf-green: #4a9a1c;
    --earth-brown: #6b4f1e;
    --brand-brown: #6a4a1a;
    --brand-green: #5aa02c;
  }
  * { margin: 0; padding: 0; box-sizing: border-box; }
  html, body { width: 1200px; height: 902px; overflow: hidden; }
  body {
    background: var(--backdrop);
    font-family: "Open Sans", Arial, sans-serif;
    color: var(--ink);
    position: relative;
  }
  .card {
    position: absolute;
    top: 291px;
    width: 540px;
    height: 320px;
    background: var(--card);
    border-radius: 10px;
    overflow: hidden;
  }
  .card--back { left: 40px; }
  .card--front { left: 620px; }

  .brand { display: flex; align-items: center; gap: 8px; }
  .brand__dot {
    width: 14px; height: 14px; border-radius: 50%;
    background: var(--brand-green);
  }
  .brand__name {
    font-weight: 700;
    color: var(--brand-brown);
    letter-spacing: 0.5px;
  }

  .card--back .brand {
    position: absolute;
    left: 0; right: 0; top: 112px;
    justify-content: center;
  }
  .card--back .brand__name { font-size: 34px; }
  .back__website {
    position: absolute;
    left: 0; right: 0; top: 178px;
    text-align: center;
    font-size: 14px;
    color: var(--ink-soft);
    letter-spacing: 0.4px;
  }

  .card--front .brand {
    position: absolute;
    left: 26px; top: 40px;
  }
  .card--front .brand__name { font-size: 26px; }

  .person {
    position: absolute;
    right: 24px; top: 50px;
    text-align: right;
  }
  .person__name { font-size: 16px; font-weight: 600; }
  .person__title { font-size: 12px; color: var(--ink-soft); margin-top: 2px; }

  .contacts {
    position: absolute;
    right: 24px; top: 198px;
    list-style: none;
    text-align: right;
    font-size: 12px;
    line-height: 18px;
    color: var(--ink-soft);
  }
  .contacts li { display: flex; justify-content: flex-end; align-items: center; gap: 5px; }
  .contacts svg { width: 10px; height: 10px; fill: var(--ink-soft); }

  .swoosh {
    position: absolute;
    left: 0; bottom: 0;
    width: 540px; height: 110px;
  }
</style>
</head>
<body>

  <section class="card card--back">
    <div class="brand">
      <span class="brand__dot"></span>
      <span class="brand__name">TerraQuestia</span>
    </div>
    <p class="back__website">www.TerraQuestia.example</p>
  </section>

  <section class="card card--front">
    <div class="brand">
      <span class="brand__dot"></span>
      <span class="brand__name">TerraQuestia</span>
    </div>

    <div class="person">
      <p class="person__name">Tova Ruth Kellerby-Doane</p>
      <p class="person__title">Executive Director</p>
    </div>

    <ul class="contacts">
      <li>123 456 7890
        <svg viewBox="0 0 10 10"><path d="M2 0.5 L4 2.5 L3 3.8 Q4.2 6 6.2 7 L7.5 6 L9.5 8 L8 9.5 Q3 9 0.5 2 Z"/></svg>
      </li>
      <li>123 456 7890
        <svg viewBox="0 0 10 10"><rect x="1" y="4" width="8" height="5"/><rect x="2.5" y="1" width="5" height="3"/></svg>
      </li>
      <li>tovark@mailcove.example
        <svg viewBox="0 0 10 10"><rect x="0.5" y="2" width="9" height="6"/></svg>
      </li>
    </ul>

    <svg class="swoosh" viewBox="0 0 540 110" preserveAspectRatio="none" aria-hidden="true">
      <path d="M0 20 C120 0 250 8 330 42 C400 74 460 98 540 110 L0 110 Z" fill="var(--leaf-green)"/>
      <path d="M0 34 C120 16 240 24 320 58 C380 86 440 104 500 110 L0 110 Z" fill="#ffffff"/>
      <path d="M0 46 C110 30 220 38 290 70 C340 92 380 104 420 110 L0 110 Z" fill="var(--earth-brown)"/>
    </svg>
  </section>

</body>
</html>
```